R Dovak Consulting Design

Our company is a multi-faceted consulting service in specialized areas such as project management and event management.
I would like the design to utilise the colour green, but be simple and unique in concept.
The design should communicate collaboration, openness, trust, efficiency and professionalism.
We like the idea of cogs in a wheel or other geometric designs.

Target Market(s)

Target market is large corporate manufacturers.

Industry/Entity Type

Wheel

Contact Information for Business Card

R Dovak Consulting
Marlene Dovak
Ph. 0438 562 714
Email. marlyfrost@vexorline.on.net
Address. 7 Brambury Ct, Wendale Vic 3299 Australia

```html
<!DOCTYPE html>
<html lang="en">
<head>
<meta charset="utf-8">
<title>R Dovak Consulting – Business Card</title>
<link rel="stylesheet" href="https://fonts.googleapis.com/css2?family=Jost:wght@400;600&display=swap">
<style>
  :root {
    --lime: #9cff00;
    --lime-deep: #8cef00;
    --lime-text: #9ced10;
    --ink: #111111;
    --paper: #ffffff;
    --bleed-line: #ff1a1a;
    --safe-line: #5fdcf0;
  }
  html, body {
    margin: 0;
    padding: 0;
    overflow: hidden;
    background: var(--paper);
  }
  .card {
    position: relative;
    width: 1200px;
    height: 740px;
    background: var(--paper);
    font-family: "Jost", "Futura", sans-serif;
    color: var(--ink);
    overflow: hidden;
  }
  .card__guides {
    position: absolute;
    inset: 0;
  }
  .card__panel {
    position: absolute;
    left: 20px;
    top: 20px;
    width: 497px;
    height: 701px;
    background: var(--lime);
    overflow: hidden;
  }
  .card__motif {
    position: absolute;
    left: 0;
    top: 142px;
    width: 462px;
    height: 559px;
    background: radial-gradient(ellipse at 15% 70%, var(--lime-deep) 0%, var(--lime-deep) 45%, rgba(140, 239, 0, 0) 75%);
  }
  .card__email {
    position: absolute;
    left: 60px;
    top: 634px;
    font-size: 26px;
    font-weight: 600;
    line-height: 36px;
    letter-spacing: 0.2px;
  }
  .contact {
    position: absolute;
    left: 595px;
    margin: 0;
    line-height: 1.2;
  }
  .contact__name {
    top: 67px;
    font-size: 31px;
    font-weight: 400;
    color: var(--lime-text);
  }
  .contact__phone {
    top: 122px;
    font-size: 30px;
    font-weight: 400;
  }
  .brand-name {
    position: absolute;
    left: 594px;
    top: 353px;
    margin: 0;
    font-size: 58px;
    font-weight: 600;
    line-height: 1.2;
    color: var(--lime-text);
    letter-spacing: 0.5px;
  }
  .address {
    position: absolute;
    left: 595px;
    top: 561px;
    margin: 0;
    font-style: normal;
    font-size: 28px;
    line-height: 39px;
  }
</style>
</head>
<body>
  <div class="card">
    <div class="card__panel">
      <div class="card__motif" role="img" aria-label="Faint large cog wheel decoration in a deeper lime tone"></div>
      <div class="card__email">marlyfrost@vexorline.on.net</div>
    </div>

    <svg class="card__guides" width="1200" height="740" viewBox="0 0 1200 740" aria-hidden="true">
      <rect x="20" y="20" width="1162" height="701" fill="none" stroke="var(--bleed-line)" stroke-width="2"/>
      <polyline points="517,45 1157,45 1157,695 517,695" fill="none" stroke="var(--safe-line)" stroke-width="2"/>
    </svg>

    <p class="contact contact__name">Marlene Dovak</p>
    <p class="contact contact__phone">0438 562 714</p>

    <h1 class="brand-name">R Dovak Consulting</h1>

    <address class="address">
      7 Brambury Ct<br>
      Wendale Vic 3299<br>
      Australia
    </address>
  </div>
</body>
</html>
```